Shopify Web-Page "Tovi-BrambleDays

We are building a new business in Switzerland offering premium sewing holiday camps for kids aged 9–14. In enclosed brief outlines our requirements for a complete Shopify homepage design and a multilingual logo creation.
Domains: tovi-brambledays.ch ; tovi-giornirovo.ch ; tovi-brombeertage.ch

Project Overview
We are looking for:
1. A modern, fully designed Shopify homepage in English using standard Shopify content blocks (no custom coding), which we can later update ourselves. Supporting Multilanguage (EN, German, Italian).

2. A logo design that includes the brand identity and communicates our multilingual, creative, and child-focused positioning.

All details in enclosed

```html
<!DOCTYPE html>
<html lang="en">
<head>
<meta charset="utf-8">
<title>Tovi-BrambleDays — Creative Sewing Camps</title>
<link href="https://fonts.googleapis.com/css2?family=Lexend:wght@400;500;600&family=Figtree:wght@400;500;600;700&display=swap" rel="stylesheet">
<style>
:root{
  --orange:#ec6608;
  --navy:#233352;
  --peach:#fdf1e8;
  --ink:#1d1d1d;
  --text:#3a3a3a;
  --muted:#8a8a8a;
  --line:#e4e4e4;
  --white:#ffffff;
}
*{margin:0;padding:0;box-sizing:border-box}
html,body{width:1200px;height:3203px;overflow:hidden}
body{font-family:"Figtree",sans-serif;color:var(--text);background:var(--white);position:relative}
h1,h2,h3{font-family:"Lexend",sans-serif;font-weight:400;color:var(--ink)}
a{color:inherit;text-decoration:none}
.btn{display:inline-flex;align-items:center;justify-content:center;font-family:"Figtree",sans-serif;font-weight:600}
.btn-solid{background:var(--orange);color:var(--white)}
.btn-pill{border-radius:26px}

/* top bar */
.topbar{position:absolute;top:0;left:0;width:1200px;height:51px;background:var(--orange);color:var(--white);font-size:16px;font-weight:500}
.topbar .item{position:absolute;top:15px;display:flex;align-items:center;gap:10px}
.topbar svg{width:18px;height:18px}

/* nav */
.nav{position:absolute;top:51px;left:0;width:1200px;height:77px;background:var(--white);border-bottom:1px solid #eee}
.brand{position:absolute;left:111px;top:14px;display:flex;align-items:center;gap:11px}
.brand-dot{width:48px;height:48px;border-radius:50%;background:var(--orange)}
.brand-name{font-family:"Lexend",sans-serif;font-weight:500;font-size:20px;color:var(--navy)}
.menu{position:absolute;left:391px;top:28px;display:flex;gap:35px;font-size:16px;font-weight:500;color:var(--ink)}
.menu .active{color:var(--orange)}
.nav-icons{position:absolute;left:1005px;top:25px;display:flex;gap:25px}

/* hero */
.hero{position:absolute;top:128px;left:0;width:1200px;height:510px;overflow:hidden;
  background:linear-gradient(90deg,#ededed 0%,#e9e8e7 40%,#e2ddd8 52%,#d4c8bc 62%)}
.hero-photo{position:absolute;left:560px;top:0;width:640px;height:510px;
  background:
    radial-gradient(ellipse 160px 130px at 330px 110px,rgba(196,150,120,.55),transparent 70%),
    radial-gradient(ellipse 200px 160px at 470px 300px,rgba(250,250,250,.75),transparent 70%),
    radial-gradient(ellipse 230px 140px at 220px 380px,rgba(220,205,190,.9),transparent 70%),
    radial-gradient(ellipse 140px 110px at 580px 430px,rgba(140,110,80,.6),transparent 70%),
    radial-gradient(ellipse 120px 200px at 90px 120px,rgba(90,75,70,.35),transparent 70%),
    linear-gradient(90deg,rgba(212,200,188,0) 0%,#c9b7a4 20%,#b7a08b 60%,#9c8671 100%)}
.hero h1{position:absolute;left:111px;top:86px;font-size:42px;line-height:52px;width:520px}
.hero p{position:absolute;left:111px;top:246px;font-size:15px;line-height:29px;width:420px;color:var(--ink)}
.hero .actions{position:absolute;left:111px;top:325px;display:flex;gap:25px}
.hero .btn{height:55px;font-size:19px}
.btn-outline{background:var(--white);color:var(--orange);width:189px}

/* about */
.about{position:absolute;top:638px;left:0;width:1200px;height:494px;background:var(--white)}
.about-photo{position:absolute;left:0;top:0;width:620px;height:494px;
  background:
    radial-gradient(ellipse 120px 200px at 70px 260px,rgba(110,75,55,.75),transparent 70%),
    radial-gradient(ellipse 110px 140px at 260px 160px,rgba(170,130,105,.7),transparent 70%),
    radial-gradient(ellipse 130px 110px at 250px 400px,rgba(235,190,200,.8),transparent 70%),
    radial-gradient(ellipse 90px 160px at 440px 270px,rgba(140,165,205,.75),transparent 70%),
    radial-gradient(ellipse 220px 90px at 300px 80px,rgba(90,90,85,.35),transparent 70%),
    linear-gradient(90deg,#a88a74 0%,#c8b09a 45%,#e4d8cc 72%,#ffffff 100%)}
.about h2{position:absolute;left:641px;top:76px;font-size:40px;line-height:44px}
.about p{position:absolute;left:643px;top:175px;width:450px;font-size:14.5px;line-height:26px;color:var(--ink)}
.about .btn{position:absolute;left:643px;top:363px;width:143px;height:51px;font-size:16px}

/* how */
.how{position:absolute;top:1132px;left:0;width:1200px;height:463px;background:var(--navy)}
.how h2{position:absolute;top:60px;width:1200px;text-align:center;color:var(--white);font-size:42px;font-weight:500}
.steps{position:absolute;left:111px;top:141px;display:flex;gap:20px}
.step{width:180px;height:232px;color:var(--white);text-align:center;padding:22px 14px}
.step h3{color:var(--white);font-size:17px;line-height:26px;font-weight:400}
.step p{font-size:11px;line-height:20px;margin-top:40px}
.s1{background:linear-gradient(rgba(0,0,0,.25),rgba(0,0,0,.25)),linear-gradient(150deg,#9a7452,#6b4e36 45%,#4a3626)}
.s2{background:linear-gradient(rgba(0,0,0,.2),rgba(0,0,0,.2)),radial-gradient(circle at 90px 150px,#e39a4a,#9b5aa0 30%,transparent 55%),linear-gradient(160deg,#2f5a44,#a23a3a 55%,#6a6a78)}
.s3{background:linear-gradient(rgba(0,0,0,.25),rgba(0,0,0,.25)),radial-gradient(circle at 60px 180px,#c79a4a,transparent 45%),linear-gradient(160deg,#4a3c32,#a88f7a 70%,#d8c8b6)}
.s4{background:linear-gradient(rgba(0,0,0,.25),rgba(0,0,0,.25)),radial-gradient(ellipse at 90px 60px,#7a6250,transparent 55%),linear-gradient(180deg,#5c4d40,#a99784 60%,#d3c6b6)}
.s5{background:linear-gradient(rgba(0,0,0,.2),rgba(0,0,0,.2)),radial-gradient(circle at 90px 150px,#c8242c,transparent 40%),linear-gradient(160deg,#7a5b48,#4a5a78 70%,#3c4a68)}

/* why */
.why{position:absolute;top:1595px;left:0;width:1200px;height:494px;background:var(--white)}
.why h2{position:absolute;left:109px;top:72px;font-size:42px;font-weight:500}
.checks{position:absolute;left:111px;top:139px;list-style:none}
.checks li{display:flex;align-items:center;gap:9px;font-size:17px;line-height:34px;color:var(--ink)}
.checks svg{width:16px;height:16px;flex:none}
.why .btn{position:absolute;left:111px;top:360px;width:142px;height:51px;font-size:16px}
.pill{position:absolute;border-radius:70px;width:132px}
.pill-a{left:714px;top:156px;height:240px;
  background:radial-gradient(ellipse 40px 60px at 70px 150px,rgba(120,120,120,.6),transparent 70%),
  linear-gradient(180deg,#f2c21c 0%,#e3a90f 45%,#d9c7a8 75%,#e6b24a 100%)}
.pill-b{left:891px;top:74px;height:236px;
  background:radial-gradient(ellipse 45px 55px at 80px 70px,rgba(220,170,140,.7),transparent 70%),
  linear-gradient(180deg,#f3e6de 0%,#f2c9d2 45%,#e7c23a 62%,#9fd3c8 100%)}

/* upcoming */
.upcoming{position:absolute;top:2089px;left:0;width:1200px;height:740px;background:var(--peach)}
.upcoming h2{position:absolute;top:60px;width:1200px;text-align:center;font-size:42px;font-weight:500}
.upcoming .lead{position:absolute;top:130px;width:1200px;text-align:center;font-size:15px;color:var(--ink)}
.camps{position:absolute;left:111px;top:183px;display:flex;gap:38px}
.camp{width:300px;height:464px;background:var(--white);border:1px solid #eadfd6}
.camp-photo{height:194px}
.c1{background:radial-gradient(ellipse 90px 60px at 150px 110px,#7fa3d8,transparent 75%),radial-gradient(ellipse 80px 40px at 70px 30px,#e8e2da,transparent 75%),linear-gradient(135deg,#c38a56,#a56c3e 60%,#c99468)}
.c2{background:radial-gradient(ellipse 90px 50px at 200px 80px,#e0a545,transparent 75%),radial-gradient(ellipse 120px 40px at 160px 170px,#6fa0c0,transparent 75%),linear-gradient(135deg,#a7abb0,#cdbfae 55%,#9aa8b4)}
.c3{background:radial-gradient(circle at 60px 60px,#2f8fb0,transparent 40%),radial-gradient(circle at 140px 120px,#8a3fa0,transparent 35%),radial-gradient(circle at 230px 140px,#5aa040,transparent 35%),radial-gradient(circle at 240px 40px,#c0582a,transparent 35%),linear-gradient(135deg,#5a4432,#3a3028)}
.camp-body{padding:20px 17px 0}
.camp h3{color:var(--orange);font-family:"Figtree",sans-serif;font-weight:600;font-size:19px}
.loc{display:flex;align-items:center;gap:7px;font-size:15px;color:var(--muted);margin-top:8px}
.loc svg{width:12px;height:14px}
.stars{display:flex;gap:2px;margin-top:7px;padding-bottom:14px;border-bottom:1px solid var(--line)}
.stars svg{width:13px;height:13px}
.camp p{font-size:12.5px;line-height:20px;color:var(--ink);padding:17px 0;border-bottom:1px solid var(--line)}
.camp .btn{margin-top:16px;width:110px;height:37px;font-size:15px;color:var(--ink)}

/* footer */
.footer{position:absolute;top:2829px;left:0;width:1200px;height:298px;background:var(--white)}
.fcol{position:absolute;top:79px}
.fcol h3{font-family:"Figtree",sans-serif;font-weight:600;font-size:19px;color:var(--ink);margin-bottom:20px}
.fcol ul{list-style:none;font-size:15px;color:var(--ink);line-height:28.5px;padding-left:4px}
.contact{font-size:15px;color:var(--ink)}
.contact div{display:flex;gap:8px;line-height:26px;margin-bottom:9px}
.contact svg{width:16px;height:16px;margin-top:5px;flex:none}
.signup{display:flex;width:246px;height:44px;border:1px solid var(--orange);align-items:center}
.signup .field{flex:1;padding-left:19px;font-size:10px;color:var(--ink);border-right:1px solid var(--line);height:28px;line-height:28px}
.signup .send{width:68px;text-align:center;font-size:11px;font-weight:600;color:var(--ink)}

.copyright{position:absolute;top:3127px;left:0;width:1200px;height:76px;background:var(--navy);color:var(--white);text-align:center;font-size:15px;line-height:76px}
</style>
</head>
<body>

<header class="topbar">
  <div class="item" style="left:111px">
    <svg viewBox="0 0 24 24" fill="none" stroke="#fff" stroke-width="2"><path d="M5 3h4l2 5-3 2a11 11 0 0 0 6 6l2-3 5 2v4a2 2 0 0 1-2 2A17 17 0 0 1 3 5a2 2 0 0 1 2-2z"/></svg>
    +41 44 555 01 99
  </div>
  <div class="item" style="left:293px">
    <svg viewBox="0 0 24 24" fill="none" stroke="#fff" stroke-width="2"><rect x="3" y="5" width="18" height="14"/><path d="M3 6l9 7 9-7"/></svg>
    info@tovi-brambledays.ch
  </div>
  <div class="item" style="left:1014px">English
    <svg viewBox="0 0 24 24" fill="none" stroke="#fff" stroke-width="2" style="width:12px"><path d="M5 9l7 7 7-7"/></svg>
  </div>
</header>

<nav class="nav">
  <div class="brand"><span class="brand-dot"></span><span class="brand-name">Tovi-BrambleDays</span></div>
  <div class="menu">
    <a class="active">Home</a><a>About Us</a><a>How the camp works</a><a>Upcoming Camp</a><a>FAQ</a>
  </div>
  <div class="nav-icons">
    <svg width="29" height="29" viewBox="0 0 29 29"><circle cx="14.5" cy="14.5" r="14.5" fill="#111"/><circle cx="13.5" cy="13.5" r="5" fill="none" stroke="#fff" stroke-width="2"/><path d="M17 17l4 4" stroke="#fff" stroke-width="2"/></svg>
    <svg width="29" height="29" viewBox="0 0 29 29" fill="none" stroke="#111" stroke-width="2"><circle cx="14.5" cy="14.5" r="13"/><circle cx="14.5" cy="11" r="4.5"/><path d="M6 23c2-4 5-6 8.5-6s6.5 2 8.5 6"/></svg>
  </div>
</nav>

<section class="hero">
  <div class="hero-photo" role="img" aria-label="Two girls sewing fabric at a white sewing machine in a bright workshop"></div>
  <h1>Tovi-BrambleDays — Creative Sewing Camps for 9–14 year olds</h1>
  <p>Mira and Lena bring over 10 years of experience teaching children sewing, tailoring and design.</p>
  <div class="actions">
    <a class="btn btn-solid" style="width:189px">Book Your Slot</a>
    <a class="btn btn-outline">View Schedule</a>
  </div>
</section>

<section class="about">
  <div class="about-photo" role="img" aria-label="Instructor helping girls with a sewing project at a workshop table"></div>
  <h2>About Tovi-BrambleDays<br>Sewing</h2>
  <p>Mira and Lena have over 10 years of experience in teaching children sewing, tailoring, and design with fun, style, and structure. In small groups (max. 8 children), we guide young talents through a creative week of vacation – with real results: self-sewn pieces, new friends, and lots of pride.At the last day, the children show off their success, their own sewn unique pieces, in a symapatic fashion show.</p>
  <a class="btn btn-solid btn-pill">Read More</a>
</section>

<section class="how">
  <h2>How The Camp Works</h2>
  <div class="steps">
    <div class="step s1" role="img" aria-label="Sewing patterns on a wooden table"><h3>Project<br>selection</h3><p style="margin-top:42px">Your child chooses their own model based on previously produced clothing items and sewing patterns.</p></div>
    <div class="step s2" role="img" aria-label="Colourful fabric swatches in front of a clothes rail"><h3>Fabric<br>selection</h3><p>High-quality fabrics are available.</p></div>
    <div class="step s3" role="img" aria-label="Sewing machine needle close-up"><h3>Sewing machine<br>operation</h3><p>Learn how to use a sewing machine</p></div>
    <div class="step s4" role="img" aria-label="Folded fabric and thread spool"><h3>Sewing &amp; refining</h3><p style="margin-top:66px">Step by step to the goal with professional guidance</p></div>
    <div class="step s5" role="img" aria-label="Child holding a finished sewn heart"><h3>Showtime!</h3><p style="margin-top:66px">Fashion show or photo shoot at the end of the week</p></div>
  </div>
</section>

<section class="why">
  <h2>Why Parents Choose Us</h2>
  <ul class="checks">
    <li><svg viewBox="0 0 16 16"><circle cx="8" cy="8" r="8" fill="#ec6608"/><path d="M4.5 8.2l2.3 2.3 4.7-4.7" stroke="#fff" stroke-width="1.8" fill="none"/></svg>Small groups &amp; personalized attention</li>
    <li><svg viewBox="0 0 16 16"><circle cx="8" cy="8" r="8" fill="#ec6608"/><path d="M4.5 8.2l2.3 2.3 4.7-4.7" stroke="#fff" stroke-width="1.8" fill="none"/></svg>Multilingual supervision (DE / EN / IT)</li>
    <li><svg viewBox="0 0 16 16"><circle cx="8" cy="8" r="8" fill="#ec6608"/><path d="M4.5 8.2l2.3 2.3 4.7-4.7" stroke="#fff" stroke-width="1.8" fill="none"/></svg>High-quality fabrics &amp; top-quality sewing machines (Stitchwell)</li>
    <li><svg viewBox="0 0 16 16"><circle cx="8" cy="8" r="8" fill="#ec6608"/><path d="M4.5 8.2l2.3 2.3 4.7-4.7" stroke="#fff" stroke-width="1.8" fill="none"/></svg>Encouragement of creativity, self-confidence, and fine motor skills</li>
    <li><svg viewBox="0 0 16 16"><circle cx="8" cy="8" r="8" fill="#ec6608"/><path d="M4.5 8.2l2.3 2.3 4.7-4.7" stroke="#fff" stroke-width="1.8" fill="none"/></svg>Safe, loving environment in Zurich, various places easy to reach</li>
    <li><svg viewBox="0 0 16 16"><circle cx="8" cy="8" r="8" fill="#ec6608"/><path d="M4.5 8.2l2.3 2.3 4.7-4.7" stroke="#fff" stroke-width="1.8" fill="none"/></svg>Pick-up Service from the Main-Station</li>
  </ul>
  <a class="btn btn-solid btn-pill">Read More</a>
  <div class="pill pill-a" role="img" aria-label="Yellow sewing machine stitching fabric"></div>
  <div class="pill pill-b" role="img" aria-label="Smiling girl holding sewing material"></div>
</section>

<section class="upcoming">
  <h2>Upcoming Camps</h2>
  <p class="lead">At the last day, the children show off their success, their own sewn unique pieces, in a symapatic fashion show.</p>
  <div class="camps">
    <article class="camp">
      <div class="camp-photo c1" role="img" aria-label="Hands holding a sewn blue plush toy with threads and scissors"></div>
      <div class="camp-body">
        <h3>Spring Camps</h3>
        <div class="loc"><svg viewBox="0 0 12 14"><path d="M6 1a4.5 4.5 0 0 1 4.5 4.5C10.5 9 6 13 6 13S1.5 9 1.5 5.5A4.5 4.5 0 0 1 6 1z" fill="none" stroke="#111" stroke-width="2"/><circle cx="6" cy="5.5" r="1.5" fill="#111"/></svg>Switzerland</div>
        <div class="stars"><svg viewBox="0 0 12 12"><path d="M6 0l1.8 3.8 4.2.5-3.1 2.9.8 4.1L6 9.3 2.3 11.3l.8-4.1L0 4.3l4.2-.5z" fill="#ec6608"/></svg><svg viewBox="0 0 12 12"><path d="M6 0l1.8 3.8 4.2.5-3.1 2.9.8 4.1L6 9.3 2.3 11.3l.8-4.1L0 4.3l4.2-.5z" fill="#ec6608"/></svg><svg viewBox="0 0 12 12"><path d="M6 0l1.8 3.8 4.2.5-3.1 2.9.8 4.1L6 9.3 2.3 11.3l.8-4.1L0 4.3l4.2-.5z" fill="#ec6608"/></svg><svg viewBox="0 0 12 12"><path d="M6 0l1.8 3.8 4.2.5-3.1 2.9.8 4.1L6 9.3 2.3 11.3l.8-4.1L0 4.3l4.2-.5z" fill="#ec6608"/></svg><svg viewBox="0 0 12 12"><path d="M6 0l1.8 3.8 4.2.5-3.1 2.9.8 4.1L6 9.3 2.3 11.3l.8-4.1L0 4.3l4.2-.5z" fill="#ec6608"/></svg></div>
        <p>Excepteur sint occaecat cupidatat non proident, sunt in culpa qui officia deserunt mollit anim id est laborum.</p>
        <a class="btn btn-solid btn-pill">Book Now</a>
      </div>
    </article>
    <article class="camp">
      <div class="camp-photo c2" role="img" aria-label="Two women cutting fabric on a workshop table"></div>
      <div class="camp-body">
        <h3>Summer Camps</h3>
        <div class="loc"><svg viewBox="0 0 12 14"><path d="M6 1a4.5 4.5 0 0 1 4.5 4.5C10.5 9 6 13 6 13S1.5 9 1.5 5.5A4.5 4.5 0 0 1 6 1z" fill="none" stroke="#111" stroke-width="2"/><circle cx="6" cy="5.5" r="1.5" fill="#111"/></svg>Switzerland</div>
        <div class="stars"><svg viewBox="0 0 12 12"><path d="M6 0l1.8 3.8 4.2.5-3.1 2.9.8 4.1L6 9.3 2.3 11.3l.8-4.1L0 4.3l4.2-.5z" fill="#ec6608"/></svg><svg viewBox="0 0 12 12"><path d="M6 0l1.8 3.8 4.2.5-3.1 2.9.8 4.1L6 9.3 2.3 11.3l.8-4.1L0 4.3l4.2-.5z" fill="#ec6608"/></svg><svg viewBox="0 0 12 12"><path d="M6 0l1.8 3.8 4.2.5-3.1 2.9.8 4.1L6 9.3 2.3 11.3l.8-4.1L0 4.3l4.2-.5z" fill="#ec6608"/></svg><svg viewBox="0 0 12 12"><path d="M6 0l1.8 3.8 4.2.5-3.1 2.9.8 4.1L6 9.3 2.3 11.3l.8-4.1L0 4.3l4.2-.5z" fill="#ec6608"/></svg><svg viewBox="0 0 12 12"><path d="M6 0l1.8 3.8 4.2.5-3.1 2.9.8 4.1L6 9.3 2.3 11.3l.8-4.1L0 4.3l4.2-.5z" fill="#ec6608"/></svg></div>
        <p>Excepteur sint occaecat cupidatat non proident, sunt in culpa qui officia deserunt mollit anim id est laborum.</p>
        <a class="btn btn-solid btn-pill">Book Now</a>
      </div>
    </article>
    <article class="camp">
      <div class="camp-photo c3" role="img" aria-label="Basket of colourful thread spools and buttons"></div>
      <div class="camp-body">
        <h3>Weekend Workshop</h3>
        <div class="loc"><svg viewBox="0 0 12 14"><path d="M6 1a4.5 4.5 0 0 1 4.5 4.5C10.5 9 6 13 6 13S1.5 9 1.5 5.5A4.5 4.5 0 0 1 6 1z" fill="none" stroke="#111" stroke-width="2"/><circle cx="6" cy="5.5" r="1.5" fill="#111"/></svg>Switzerland</div>
        <div class="stars"><svg viewBox="0 0 12 12"><path d="M6 0l1.8 3.8 4.2.5-3.1 2.9.8 4.1L6 9.3 2.3 11.3l.8-4.1L0 4.3l4.2-.5z" fill="#ec6608"/></svg><svg viewBox="0 0 12 12"><path d="M6 0l1.8 3.8 4.2.5-3.1 2.9.8 4.1L6 9.3 2.3 11.3l.8-4.1L0 4.3l4.2-.5z" fill="#ec6608"/></svg><svg viewBox="0 0 12 12"><path d="M6 0l1.8 3.8 4.2.5-3.1 2.9.8 4.1L6 9.3 2.3 11.3l.8-4.1L0 4.3l4.2-.5z" fill="#ec6608"/></svg><svg viewBox="0 0 12 12"><path d="M6 0l1.8 3.8 4.2.5-3.1 2.9.8 4.1L6 9.3 2.3 11.3l.8-4.1L0 4.3l4.2-.5z" fill="#ec6608"/></svg><svg viewBox="0 0 12 12"><path d="M6 0l1.8 3.8 4.2.5-3.1 2.9.8 4.1L6 9.3 2.3 11.3l.8-4.1L0 4.3l4.2-.5z" fill="#ec6608"/></svg></div>
        <p>Excepteur sint occaecat cupidatat non proident, sunt in culpa qui officia deserunt mollit anim id est laborum.</p>
        <a class="btn btn-solid btn-pill">Book Now</a>
      </div>
    </article>
  </div>
</section>

<footer class="footer">
  <div class="fcol" style="left:111px">
    <h3>Our Location</h3>
    <div class="contact">
      <div><svg viewBox="0 0 16 16" fill="none" stroke="#111" stroke-width="1.3"><path d="M8 1a5 5 0 0 1 5 5c0 4-5 9-5 9S3 10 3 6a5 5 0 0 1 5-5z"/><circle cx="8" cy="6" r="1.8"/></svg><span>Tovi-BrambleDays<br>Switzerland</span></div>
      <div><svg viewBox="0 0 24 24" fill="none" stroke="#111" stroke-width="1.6"><path d="M5 3h4l2 5-3 2a11 11 0 0 0 6 6l2-3 5 2v4a2 2 0 0 1-2 2A17 17 0 0 1 3 5a2 2 0 0 1 2-2z"/></svg><span>+41 44 555 01 99</span></div>
      <div style="margin-top:14px"><svg viewBox="0 0 24 24" fill="none" stroke="#111" stroke-width="1.6"><rect x="3" y="5" width="18" height="14"/><path d="M3 6l9 7 9-7"/></svg><span>hello@tovi-brambledays.ch</span></div>
    </div>
  </div>
  <div class="fcol" style="left:385px">
    <h3>Quick Links</h3>
    <ul><li>Home</li><li>About Us</li><li>How the camp works</li><li>Upcoming Events</li><li>Contact Us</li></ul>
  </div>
  <div class="fcol" style="left:625px">
    <h3>Help Links</h3>
    <ul><li>FAQ</li><li>Terms of Use</li><li>Privacy Policy</li><li>Support Links</li><li>Terms &amp; Conditions</li></ul>
  </div>
  <div class="fcol" style="left:844px">
    <h3>Sign Up</h3>
    <div class="signup"><span class="field">Your Email Address</span><span class="send">SEND</span></div>
  </div>
</footer>

<div class="copyright">Copyrights@2025.Tovi-BrambleDays.All Rights Reserved</div>

</body>
</html>
```